Logo with Stationery Design Project-

The company is an on-line service for assisting the people that are in a foreclosure situation with their homes. We are presently building the site on WebPelican with Wordpress.

The best option to save a home in the USA at the end of the line with the banks is to file for bankruptcy Chapter 7 or Chapter 13. We work with homeowners and attorneys to prepare the financial package for the attorneys to negotiate with the banks after filing for bankruptcy. We also sell a binder on-line which is called the keystone relief set and the web site is: www.keystonereliefset-example.com
We need a logo and stationnary to communicate the message of advisors in the field of financial strategies when it comes to the foreclosure and bankruptcy process. This stationnary will be printed on high quality paper with the business cards being on 100 stock which is high quality in the USA.

We would like to see the logo to use the Navy blue and Aqua Green colors. The final desing should communicate the financial knowledge and promise of a light at the end of the tunnell.

The card should use both sides with the back side being the logo and the web site address that links with the front of the card. Letterhead and envelopes should be serious but sexy!

A challenge that I am sure someone is up to........

Target Market(s)

12 million people that are in foreclosure in the USA and all of the law firms that deal with foreclosure and bankruptcies in the USA all 50 states

Industry/Entity Type

Financial

Requirements
Must have
• Colors are important = Navy blue and Aqua green

```html
<!DOCTYPE html>
<html lang="en">
<head>
<meta charset="utf-8">
<title>Keystone Relief Set – Business Card</title>
<link rel="stylesheet" href="https://fonts.googleapis.com/css2?family=Source+Sans+3:wght@400;600&display=swap">
<style>
  :root {
    --backdrop: #c4b59c;
    --navy: #1b3a5c;
    --aqua: #2e9593;
    --aqua-light: #4fb0aa;
    --paper: #ffffff;
    --house-tint: #e9f3f3;
  }
  * { box-sizing: border-box; margin: 0; padding: 0; }
  html, body {
    width: 1200px;
    height: 848px;
    overflow: hidden;
    background: var(--backdrop);
    font-family: "Source Sans 3", "Myriad Pro", sans-serif;
    color: var(--navy);
  }
  .canvas {
    position: relative;
    width: 1200px;
    height: 848px;
  }
  .card {
    position: absolute;
    top: 266px;
    width: 540px;
    height: 316px;
    overflow: hidden;
  }
  .card--back {
    left: 40px;
    background: radial-gradient(ellipse at 50% 38%, var(--aqua-light) 0%, var(--aqua) 70%);
  }
  .card--front {
    left: 620px;
    background: var(--paper);
  }
  .band-navy {
    position: absolute;
    left: 0; right: 0;
    top: 81%;
    height: 9.5%;
    background: var(--navy);
  }
  .band-aqua {
    position: absolute;
    left: 0; right: 0;
    top: 80.5%;
    height: 9.5%;
    background: var(--aqua);
  }
  .brand-mark {
    position: absolute;
    left: 0; right: 0;
    top: 104px;
    text-align: center;
    font-size: 30px;
    font-weight: 400;
    color: var(--navy);
    letter-spacing: 0.5px;
  }
  .web-address {
    position: absolute;
    left: 0; right: 0;
    top: 186px;
    text-align: center;
    font-size: 20px;
    color: var(--navy);
  }
  .houses {
    position: absolute;
    left: 22px;
    top: 154px;
    width: 254px;
    height: 101px;
    background: linear-gradient(180deg, var(--paper) 0%, var(--house-tint) 100%);
  }
  .person {
    position: absolute;
    left: 262px;
    top: 62px;
  }
  .person__name {
    font-size: 22px;
    font-weight: 400;
    line-height: 1.1;
  }
  .person__role {
    font-size: 13.5px;
    line-height: 1.3;
  }
  .contact-list {
    position: absolute;
    left: 274px;
    top: 131px;
    list-style: none;
    font-size: 11.5px;
    line-height: 18px;
  }
  .contact-list li {
    display: flex;
    align-items: center;
    gap: 8px;
  }
  .contact-list svg {
    width: 10px;
    height: 10px;
    flex: none;
  }
</style>
</head>
<body>
<main class="canvas">

  <section class="card card--back" aria-label="Business card back">
    <div class="brand-mark">Keystone Relief Set</div>
    <div class="web-address">www.keystonereliefset-example.com</div>
    <div class="band-navy"></div>
  </section>

  <section class="card card--front" aria-label="Business card front">
    <div class="person">
      <div class="person__name">Name Surname</div>
      <div class="person__role">on-line service</div>
    </div>
    <ul class="contact-list">
      <li>
        <svg viewBox="0 0 10 10" aria-hidden="true"><path d="M1 3.5 Q5 1 9 3.5 L8 5 L6.5 4.3 L6.5 3.5 Q5 3 3.5 3.5 L3.5 4.3 L2 5 Z M2 6 H8 V9 H2 Z" fill="none" stroke="currentColor" stroke-width="0.9"/></svg>
        <span>123/ 456-789</span>
      </li>
      <li>
        <svg viewBox="0 0 10 10" aria-hidden="true"><circle cx="5" cy="5" r="4" fill="none" stroke="currentColor" stroke-width="1"/><path d="M1 5 H9 M5 1 V9" stroke="currentColor" stroke-width="0.8"/></svg>
        <span>www.keystonereliefset-example.com</span>
      </li>
      <li>
        <svg viewBox="0 0 10 10" aria-hidden="true"><circle cx="5" cy="5" r="4" fill="none" stroke="currentColor" stroke-width="1"/><circle cx="5" cy="5" r="1.6" fill="none" stroke="currentColor" stroke-width="1"/></svg>
        <span>name@mail.com</span>
      </li>
    </ul>
    <div class="houses" role="img" aria-label="Line drawing of a row of three house outlines"></div>
    <div class="band-aqua"></div>
  </section>

</main>
</body>
</html>
```